Harbor Zentrik needs a new Website Design

We need a WEB site landing page (/template) design, we currently have a company logo.We like the Valtor.com web designEnclosed is our company logo.Our Current website is https://www.harborzentrik.com.au/

1 page

```html
<!DOCTYPE html>
<html lang="en">
<head>
<meta charset="utf-8">
<title>Harbor Zentrik – Unified Communications</title>
<link href="https://fonts.googleapis.com/css2?family=Roboto:wght@300;400;500;700&display=swap" rel="stylesheet">
<style>
:root{
  --blue:#1b9bd7;
  --blue-dark:#1079b0;
  --ink:#2a2a2a;
  --muted:#6d6d6d;
  --light:#f2f2f2;
  --white:#ffffff;
  --footer:#1e1e1e;
  --footer-text:#9a9a9a;
}
*{box-sizing:border-box;margin:0;padding:0}
html,body{width:1200px;height:4212px;overflow:hidden}
body{font-family:'Roboto',Arial,sans-serif;color:var(--ink);background:var(--white);position:relative}
.section{position:absolute;left:0;width:1200px}
.btn{display:inline-block;background:var(--blue);color:var(--white);font-size:13px;font-weight:500;padding:11px 22px;border-radius:2px}
.btn.ghost{background:rgba(255,255,255,.12);border:1px solid rgba(255,255,255,.5)}
.placeholder{position:absolute;border-radius:6px}

/* hero */
.hero{top:0;height:540px;background:linear-gradient(180deg,#3b4149 0%,#23272d 100%);overflow:hidden}
.hero-photo{position:absolute;left:300px;top:0;width:900px;height:540px;background:linear-gradient(90deg,rgba(43,47,54,0) 0%,#4d545c 45%,#3a3f46 100%)}
.topbar{position:absolute;top:24px;right:40px;display:flex;gap:8px}
.topbar span{font-size:11px;color:var(--white);padding:6px 12px;border-radius:2px;background:var(--blue)}
.topbar span.alt{background:#3d444c}
.brand{position:absolute;left:60px;top:66px;display:flex;align-items:center;gap:10px;font-size:24px;font-weight:700;color:var(--white)}
.brand i{width:14px;height:14px;background:var(--blue);border-radius:50%}
.nav{position:absolute;left:390px;top:70px;display:flex;gap:34px;font-size:14px;color:var(--white)}
.hero h1{position:absolute;left:100px;top:284px;width:640px;font-size:38px;line-height:1.2;font-weight:700;color:var(--white);letter-spacing:-.3px}
.hero .lead{position:absolute;left:100px;top:386px;font-size:15px;color:#d8d8d8}
.hero .actions{position:absolute;left:100px;top:446px;display:flex;gap:14px}

/* features */
.features{top:540px;height:640px;text-align:center}
.features h2{width:680px;margin:120px auto 0;font-size:38px;line-height:1.2;font-weight:500;color:var(--blue)}
.features .sub{margin-top:18px;font-size:15px;color:var(--muted)}
.icons{position:absolute;top:340px;left:120px;width:960px;display:flex;justify-content:space-between}
.icon{width:130px;text-align:center}
.icon svg{width:76px;height:76px}
.icon p{margin-top:14px;font-size:11px;font-weight:500;text-transform:uppercase;color:var(--ink);line-height:1.4}

/* service rows */
.row{height:480px}
.row.grey{background:var(--light)}
.copy{position:absolute;width:420px}
.copy h3{font-size:15px;font-weight:700;color:var(--blue);text-transform:uppercase;margin-bottom:16px}
.copy h4{font-size:13px;font-weight:700;margin-bottom:12px}
.copy p{font-size:12.5px;line-height:1.6;color:var(--muted);margin-bottom:12px}
.copy .btn{margin-top:10px}

/* split */
.split{top:3120px;height:360px;display:flex}
.split .half{width:600px;height:360px;position:relative;color:var(--white);text-align:center;padding-top:80px}
.voice{background:linear-gradient(135deg,#4fb5e6 0%,#1b8fc8 100%)}
.support{background:linear-gradient(135deg,#2f6f96 0%,#1f4f6e 100%)}
.split h3{font-size:15px;font-weight:700;text-transform:uppercase;margin-bottom:16px}
.split p{font-size:12.5px;line-height:1.6;width:400px;margin:0 auto 22px;color:#eaf6fc}
.split .btn{background:var(--white);color:var(--blue)}

/* partners */
.partners{top:3480px;height:468px;text-align:center}
.partners h2{margin-top:64px;font-size:36px;font-weight:500;color:var(--blue)}
.partners .sub{width:700px;margin:16px auto 0;font-size:13px;line-height:1.6;color:var(--muted)}
.social{position:absolute;left:100px;top:196px;display:flex;gap:10px}
.social i{width:12px;height:12px;border-radius:50%;background:var(--blue)}
.badges{position:absolute;top:246px;left:150px;width:900px;display:flex;justify-content:space-between;align-items:center}
.badges div{background:#dcdcdc;border-radius:4px}
.dots{position:absolute;top:396px;left:0;width:1200px;display:flex;justify-content:center;gap:8px}
.dots i{width:7px;height:7px;border-radius:50%;background:#cfcfcf}
.dots i.on{background:#7a7a7a}

/* footer */
.footer{top:3948px;height:264px;background:var(--footer);color:var(--footer-text)}
.fcol{position:absolute;top:36px}
.fcol h5{font-size:12px;font-weight:700;color:var(--white);text-transform:uppercase;margin-bottom:12px}
.fcol p{font-size:11px;line-height:1.65}
.subscribe{display:flex;margin-top:14px}
.subscribe span{width:220px;height:28px;background:var(--white);font-size:11px;color:#999;padding:7px 10px}
.subscribe b{background:var(--blue);color:var(--white);font-size:11px;font-weight:500;padding:7px 14px}
.copyright{position:absolute;bottom:0;left:0;width:1200px;height:34px;border-top:1px solid #333;font-size:10px;text-align:center;line-height:34px}
</style>
</head>
<body>

<header class="section hero">
  <div class="hero-photo" role="img" aria-label="Photo of a business team standing in an office"></div>
  <div class="topbar"><span>Log in</span><span class="alt">Sign up</span></div>
  <div class="brand"><i></i>Harbor Zentrik</div>
  <nav class="nav"><span>Home</span><span>About ▾</span><span>Data</span><span>Hardware ▾</span><span>Service Requests ▾</span><span>Terms &amp; Conditions ▾</span><span>Status</span></nav>
  <h1>Australia's Business Grade Unified Communications Company</h1>
  <p class="lead">White Label Solution for all your Communication Needs</p>
  <div class="actions"><span class="btn">Read More ›</span><span class="btn ghost">Remote Support Access ›</span></div>
</header>

<section class="section features">
  <h2>Liberating Businesses from Traditional Communications System</h2>
  <p class="sub">We have all the components to start to run your own White Label Telco</p>
  <div class="icons">
    <div class="icon"><svg viewBox="0 0 76 76" fill="none" stroke="#2a2a2a" stroke-width="2"><path d="M20 50h38a12 12 0 0 0-2-24 16 16 0 0 0-30 4 10 10 0 0 0-6 20z" fill="#cfe9f7"/><path d="M38 50v12M28 62h20"/></svg><p>Cloud IP PBX</p></div>
    <div class="icon"><svg viewBox="0 0 76 76" fill="none" stroke="#2a2a2a" stroke-width="2"><rect x="10" y="14" width="36" height="26" rx="3" fill="#cfe9f7"/><rect x="30" y="34" width="36" height="24" rx="3" fill="#fff"/><path d="M36 44h24M36 50h16"/></svg><p>Unified<br>Communications</p></div>
    <div class="icon"><svg viewBox="0 0 76 76" fill="none" stroke="#2a2a2a" stroke-width="2"><rect x="18" y="10" width="36" height="52" rx="2" fill="#fff"/><path d="M26 22h20M26 30h20M26 38h12"/><circle cx="50" cy="54" r="10" fill="#cfe9f7"/><path d="M46 54l3 3 6-6"/></svg><p>Invoice &amp;<br>Payment Platform</p></div>
    <div class="icon"><svg viewBox="0 0 76 76" fill="none" stroke="#2a2a2a" stroke-width="2"><rect x="16" y="12" width="44" height="14" rx="2" fill="#cfe9f7"/><rect x="16" y="30" width="44" height="14" rx="2" fill="#fff"/><rect x="16" y="48" width="44" height="14" rx="2" fill="#cfe9f7"/><circle cx="24" cy="19" r="2"/><circle cx="24" cy="37" r="2"/><circle cx="24" cy="55" r="2"/></svg><p>Data<br>Services</p></div>
    <div class="icon"><svg viewBox="0 0 76 76" fill="none" stroke="#2a2a2a" stroke-width="2"><rect x="14" y="14" width="48" height="40" rx="3" fill="#cfe9f7"/><path d="M30 62h16M38 54v8"/><path d="M28 30c4 8 12 14 20 14l3-5-6-3-3 3c-3-1-6-4-7-7l3-3-3-6z" fill="#fff"/></svg><p>Voice<br>Services</p></div>
    <div class="icon"><svg viewBox="0 0 76 76" fill="none" stroke="#2a2a2a" stroke-width="2"><path d="M20 58l24-24a10 10 0 0 1 12-14l-6 6 2 6 6 2 6-6a10 10 0 0 1-14 12L26 64z" fill="#cfe9f7"/><path d="M18 18l16 16M14 22l8-8"/></svg><p>Support</p></div>
  </div>
</section>

<section class="section row grey" style="top:1180px">
  <div class="copy" style="left:100px;top:140px">
    <h3>Cloud IP PBX</h3>
    <h4>Multiple IP PBXs on a single instance</h4>
    <p>A White Label Cloud PBX is able to handle multiple customers (tenants) with a single instance of the software. Even though every customer has a dedicated PBX, they all share the same physical instance. Using the single instance for all customers cuts down operating costs significantly.</p>
    <span class="btn">Read More ›</span>
  </div>
  <div class="placeholder" role="img" aria-label="Desktop monitor showing the PBX dashboard" style="left:740px;top:20px;width:400px;height:420px;background:linear-gradient(160deg,#e9e9e9,#bfc4c8)"></div>
</section>

<section class="section row" style="top:1660px">
  <div class="placeholder" role="img" aria-label="Two smartphones showing the communications app" style="left:100px;top:20px;width:320px;height:440px;background:linear-gradient(160deg,#f1f1f1,#c9ced2)"></div>
  <div class="copy" style="left:552px;top:130px">
    <h3>Unified Communications</h3>
    <h4>Available on Desktop &amp; Mobile</h4>
    <p>Communicator is a Desktop &amp; Mobile Unified Communications application designed to provide business users with a set of features and benefits capable of transforming your company communication system into a unified experience.</p>
    <p>It is available on all major desktop operating systems as a desktop application, and on the leading phone platforms as a mobile application.</p>
    <span class="btn">Read More ›</span>
  </div>
</section>

<section class="section row grey" style="top:2140px">
  <div class="copy" style="left:100px;top:150px">
    <h3>Invoice &amp; Payment Platform</h3>
    <h4>All places to search to run your management</h4>
    <p>Invoice Portal is a fully featured telecom customer portal designed for integration with one or more Cloud PBX telephony switches. Invoice Portal has a friendly GUI that enables efficient, automated billing, invoicing and payments, allowing you to spend less time dealing with the administration of your company and more time in it.</p>
    <span class="btn">Read More ›</span>
  </div>
  <div class="placeholder" role="img" aria-label="Desktop monitor showing the invoice platform" style="left:740px;top:30px;width:400px;height:420px;background:linear-gradient(160deg,#e9e9e9,#bfc4c8)"></div>
</section>

<section class="section row" style="top:2620px;height:500px">
  <div class="placeholder" role="img" aria-label="Laptop with a glowing cloud above it" style="left:100px;top:40px;width:360px;height:420px;background:linear-gradient(160deg,#cde9f8,#3ca4dc)"></div>
  <div class="copy" style="left:552px;top:160px">
    <h3>Data Services</h3>
    <p>Data Services * - our all services available all over:</p>
    <p>Fibre<br>Ethernet – business grade and dedicated<br>Broadband – choose from fast and fastest speeds all with unlimited download</p>
    <span class="btn">Read More ›</span>
  </div>
</section>

<section class="section split">
  <div class="half voice" role="img" aria-label="Blue photo of a person on a headset call">
    <h3>Voice Services</h3>
    <p>Everything for your business: Cloud PBX, Inbound Numbers, Call Recording, SIP Trunks, Phone Number Porting, Virtual Fax, Mobile and Conference, with 24/7 support included.</p>
    <span class="btn">Read More ›</span>
  </div>
  <div class="half support" role="img" aria-label="Photo of a support team at work">
    <h3>Support</h3>
    <p>We are here to help. Our technical support team is able to assist with remote sessions and onsite visits across the country.</p>
    <span class="btn">Read More ›</span>
  </div>
</section>

<section class="section partners">
  <h2>Meet Our Partners</h2>
  <p class="sub">Lorem ipsum, or lipsum as it is sometimes known, is dummy text used in laying out print, graphic or web designs. The passage is attributed to an unknown typesetter in the 15th century who is thought to have scrambled parts.</p>
  <div class="social"><i></i><i></i><i></i></div>
  <div class="badges">
    <div style="width:70px;height:56px"></div>
    <div style="width:90px;height:56px"></div>
    <div style="width:130px;height:56px"></div>
    <div style="width:120px;height:56px"></div>
    <div style="width:140px;height:56px"></div>
    <div style="width:90px;height:56px"></div>
  </div>
  <div class="dots"><i></i><i></i><i class="on"></i><i></i><i></i></div>
</section>

<footer class="section footer">
  <div class="fcol" style="left:100px">
    <h5>Contact Us</h5>
    <p>ABN 12 345 678 901<br>PO Box 114, Kingston NSW 2600<br>General: support@harborzentrik.com.au<br>Sales: sales@harborzentrik.com.au<br>Phone: 1300 555 014 / +61 2 5550 1420</p>
  </div>
  <div class="fcol" style="left:500px">
    <h5>Stay Connected</h5>
    <p>Subscribe to our newsletter to receive news,<br>offers and updates straight to your inbox.</p>
    <div class="subscribe"><span>Email address</span><b>Sign Up</b></div>
  </div>
  <div class="fcol" style="left:960px">
    <h5>Navigate</h5>
    <p>Home<br>About<br>Data<br>Hardware<br>Service Requests<br>Terms &amp; Conditions<br>Status</p>
  </div>
  <div class="copyright">Copyright © 2024 Harbor Zentrik. All rights reserved.</div>
</footer>

</body>
</html>
```